Business Card Design for Marketing Firm

Looking for business card design for higher end marketing firm. Clean but impressionable/trendy. We are a marketing firm that represents manufacturers in the foodservice equipment and supply industry. Our customers are end users such has hotels, restaurants, country clubs, convention centers and casinos as well as distributors of restaurants supplies and equipment, and manufacturers of foodservice equipment and supplies.
Target Market(s)
Hotels, Restaurants, Supply & Equipment Distributors, Foodservice Manufacturers
Industry/Entity Type
Foodservice/Hospitality
Contact Information for Business Card
Name, Title, Contact Number, Email, Website, Social Media, Address
Requirements
Must have
- Clean & Simple but Serious and Impressionable

```html
<!DOCTYPE html>
<html lang="en">
<head>
<meta charset="utf-8">
<title>Summit Foodservice Reps — Business Cards</title>
<link href="https://fonts.googleapis.com/css2?family=Montserrat:wght@400;700&display=swap" rel="stylesheet">
<style>
  :root {
    --navy: #2b2a7a;
    --ink: #222;
    --paper: #ffffff;
    --backdrop: #adaeae;
  }
  * { box-sizing: border-box; margin: 0; padding: 0; }
  html, body { width: 1200px; height: 900px; overflow: hidden; }
  body {
    background: var(--backdrop);
    position: relative;
    font-family: "Montserrat", sans-serif;
    color: var(--ink);
  }
  .card {
    position: absolute;
    width: 525px;
    height: 300px;
    background: var(--paper);
    border-radius: 18px;
    box-shadow: 0 4px 0 var(--navy), 0 10px 22px rgba(0,0,0,.18);
  }
  .card--front { left: 80px; top: 80px; }
  .card--back  { left: 595px; top: 520px; }

  .brand {
    position: absolute;
    display: flex;
    align-items: center;
    gap: 12px;
    font-family: "Montserrat", sans-serif;
    font-weight: 400;
    color: var(--navy);
    white-space: nowrap;
  }
  .brand__mark {
    flex: none;
    border: 2px solid var(--navy);
    border-radius: 50%;
  }
  .brand__name { line-height: 1.2; }

  .card--front .brand { left: 50%; top: 50%; transform: translate(-50%, -50%); }
  .card--front .brand__mark { width: 34px; height: 34px; }
  .card--front .brand__name { font-size: 24px; }

  .card--back .brand { left: 30px; top: 128px; gap: 8px; }
  .card--back .brand__mark { width: 20px; height: 20px; border-width: 1.5px; }
  .card--back .brand__name { font-size: 12.5px; }

  .contact {
    position: absolute;
    left: 268px; top: 62px;
    padding-left: 14px;
    border-left: 1.5px solid var(--navy);
    height: 150px;
  }
  .contact__name { font-weight: 700; font-size: 19px; color: var(--navy); line-height: 1.1; }
  .contact__title { font-size: 11px; margin-top: 2px; }
  .contact__address { font-size: 11px; line-height: 1.35; margin-top: 9px; }
  .contact__list { list-style: none; margin-top: 10px; }
  .contact__list li { display: flex; align-items: center; gap: 8px; font-size: 11px; line-height: 1.55; }
  .contact__list svg { width: 11px; height: 11px; fill: var(--navy); flex: none; }

  .social {
    position: absolute;
    left: 330px; top: 240px;
    display: flex; gap: 6px;
  }
  .social span { width: 13px; height: 13px; border-radius: 3px; background: var(--navy); }
</style>
</head>
<body>

  <section class="card card--front" aria-label="Card front">
    <div class="brand">
      <span class="brand__mark"></span>
      <span class="brand__name">Summit Foodservice Reps</span>
    </div>
  </section>

  <section class="card card--back" aria-label="Card back">
    <div class="brand">
      <span class="brand__mark"></span>
      <span class="brand__name">Summit Foodservice Reps</span>
    </div>

    <div class="contact">
      <p class="contact__name">Daniel Marsh</p>
      <p class="contact__title">Owner</p>
      <p class="contact__address">415 Harbor Ave. Suite 210<br>Ridgeview, CO 80210</p>
      <ul class="contact__list">
        <li><svg viewBox="0 0 24 24" aria-hidden="true"><path d="M6.6 10.8a15 15 0 0 0 6.6 6.6l2.2-2.2a1 1 0 0 1 1-.25 11.4 11.4 0 0 0 3.6.57 1 1 0 0 1 1 1V20a1 1 0 0 1-1 1A17 17 0 0 1 3 4a1 1 0 0 1 1-1h3.5a1 1 0 0 1 1 1c0 1.25.2 2.45.57 3.57a1 1 0 0 1-.25 1z"/></svg>(555) 214-0387</li>
        <li><svg viewBox="0 0 24 24" aria-hidden="true"><path d="M7 1h10a2 2 0 0 1 2 2v18a2 2 0 0 1-2 2H7a2 2 0 0 1-2-2V3a2 2 0 0 1 2-2zm0 3v14h10V4zm5 15.5a1.2 1.2 0 1 0 0 2.4 1.2 1.2 0 0 0 0-2.4z"/></svg>(555) 214-0387</li>
        <li><svg viewBox="0 0 24 24" aria-hidden="true"><path d="M2 5h20v14H2zm2 2v.5l8 5 8-5V7z"/></svg>info@summitfoodreps.com</li>
        <li><svg viewBox="0 0 24 24" aria-hidden="true"><circle cx="12" cy="12" r="10"/></svg>www.summitfoodreps.com</li>
      </ul>
    </div>

    <div class="social" aria-label="Social profiles">
      <span></span><span></span><span></span>
    </div>
  </section>

</body>
</html>
```